Mechanical Engineer Business Card Design (Unemployed)

I am unemployed and actively looking for a job in Canada. I will be using this business card when I meet potential employers or in networking events.I would love to have the engraved writing style (as if it is engraved on the card). Some examples attached.I would love to have a personalized logo that represents my 2 majors. The final design should have a professional look that can stand out if attached to a resume. Jobs I am applying for are in construction, mining, oil and gas, Aerospace, manufacturing and whatever field I can be integrated in.A metallic look on the back is ok. but the front have to be sort of can be written on. you can also try to add my linkedin profile https://ca.folionet.example/in/doruvelsh
On the front or back, I would love to have the symbol of mail and phone rather than the words. that saves spaceAmaze me guys.

Target Market(s)

Engineering

Industry/Entity Type

Engineering

Contact Information for Business Card

Doru Velsh
Mechanical Engineer

Phone number: +1 (555) 014 - 2736
email: velshdoru@mailbrook.example

Font styles to use
Serif
Sans Serif
Decorative
Script

Requirements
Must have
• PERSONALIZED and brand new Simple Logo
• Professional look
• Engraved writing for the name
• Help stand out when attached on CV
Nice to have
• Metallic back look

```html
<!DOCTYPE html>
<html lang="en">
<head>
<meta charset="utf-8">
<title>Doru Velsh — Business Card</title>
<link href="https://fonts.googleapis.com/css2?family=Open+Sans:wght@400;600&display=swap" rel="stylesheet">
<style>
  :root {
    --backdrop: #2a2c2f;
    --card: #1d2125;
    --card-edge: #15181b;
    --ink: #4c535b;
    --ink-highlight: rgba(255, 255, 255, 0.10);
    --ink-shade: rgba(0, 0, 0, 0.85);
    --rule: #3f454c;
  }
  * { box-sizing: border-box; margin: 0; padding: 0; }
  html, body {
    width: 1200px;
    height: 1189px;
    overflow: hidden;
    background: var(--backdrop);
    font-family: "Open Sans", Arial, sans-serif;
  }
  .stage { position: relative; width: 1200px; height: 1189px; }

  .card {
    position: absolute;
    left: 170px;
    width: 860px;
    height: 490px;
    background: var(--card);
    border-radius: 26px;
    box-shadow: 0 0 0 1px var(--card-edge), 0 18px 40px rgba(0, 0, 0, 0.45);
  }
  .card--back { top: 70px; }
  .card--front { top: 630px; }

  .engraved {
    color: var(--ink);
    text-shadow: 0 -1px 0 var(--ink-shade), 0 1px 0 var(--ink-highlight);
  }
  .mark-dot {
    display: block;
    border-radius: 50%;
    border: 3px solid var(--ink);
    box-shadow: 0 1px 0 var(--ink-highlight), inset 0 2px 2px var(--ink-shade);
  }

  /* back side */
  .back__lockup {
    position: absolute;
    left: 150px;
    top: 170px;
    display: flex;
    align-items: center;
    gap: 26px;
  }
  .back__lockup .mark-dot { width: 96px; height: 96px; }
  .back__name {
    font-size: 56px;
    font-weight: 400;
    letter-spacing: 1px;
  }
  .back__url {
    position: absolute;
    left: 150px;
    top: 310px;
    font-size: 22px;
    font-weight: 600;
    letter-spacing: 0.3px;
  }

  /* front side */
  .front__mark {
    position: absolute;
    left: 60px;
    top: 0;
    width: 340px;
    height: 490px;
    display: flex;
    align-items: center;
    justify-content: center;
  }
  .front__mark .mark-dot { width: 190px; height: 190px; }
  .front__divider {
    position: absolute;
    left: 415px;
    top: 60px;
    width: 2px;
    height: 370px;
    background: var(--rule);
    box-shadow: -1px 0 0 var(--ink-shade), 1px 0 0 var(--ink-highlight);
  }
  .front__details {
    position: absolute;
    left: 460px;
    top: 70px;
  }
  .front__name {
    font-size: 34px;
    font-weight: 400;
    letter-spacing: 1px;
    line-height: 1.1;
  }
  .front__title {
    font-size: 20px;
    font-weight: 600;
    margin-bottom: 14px;
  }
  .front__degree {
    font-size: 20px;
    font-weight: 600;
    line-height: 1.4;
  }
  .contact-list { list-style: none; margin-top: 80px; }
  .contact-list li {
    display: flex;
    align-items: center;
    gap: 12px;
    font-size: 20px;
    line-height: 1.5;
  }
  .contact-icon {
    width: 22px;
    height: 22px;
    flex: none;
    filter: drop-shadow(0 1px 0 rgba(255,255,255,0.10));
  }
</style>
</head>
<body>
<main class="stage">

  <section class="card card--back" aria-label="Card back">
    <div class="back__lockup">
      <span class="mark-dot" aria-hidden="true"></span>
      <h1 class="back__name engraved">Doru Velsh</h1>
    </div>
    <p class="back__url engraved">https://ca.folionet.example/in/doruvelsh</p>
  </section>

  <section class="card card--front" aria-label="Card front">
    <div class="front__mark">
      <span class="mark-dot" aria-hidden="true"></span>
    </div>
    <div class="front__divider"></div>
    <div class="front__details">
      <h2 class="front__name engraved">Doru Velsh</h2>
      <p class="front__title engraved">Field Mechanical Engineer</p>
      <p class="front__degree engraved">Mechanical Engineer (B.Sc.)</p>
      <p class="front__degree engraved">Aerospace Engineer (M.Sc.)</p>
      <ul class="contact-list">
        <li class="engraved">
          <svg class="contact-icon" viewBox="0 0 22 22" aria-hidden="true">
            <rect x="1" y="1" width="20" height="20" rx="4" fill="none" stroke="#4c535b" stroke-width="2"/>
            <path d="M7 5c1 0 2 2.5 2 3s-1.2 1-1 1.8c.6 1.6 1.8 2.8 3.2 3.4.8.2 1.2-1 1.8-1s3 1 3 2-1.5 2.3-2.5 2.3C9 16.5 5.5 13 5.5 7.5 5.5 6 6.3 5 7 5z" fill="#4c535b"/>
          </svg>
          +1 (555) 014 - 2736
        </li>
        <li class="engraved">
          <svg class="contact-icon" viewBox="0 0 22 22" aria-hidden="true">
            <rect x="1" y="1" width="20" height="20" rx="4" fill="none" stroke="#4c535b" stroke-width="2"/>
            <rect x="5" y="7" width="12" height="9" fill="none" stroke="#4c535b" stroke-width="1.6"/>
            <path d="M5 7l6 5 6-5" fill="none" stroke="#4c535b" stroke-width="1.6"/>
          </svg>
          velshdoru@mailbrook.example
        </li>
      </ul>
    </div>
  </section>

</main>
</body>
</html>
```